DL size flyer for Autism Consultancy website

We need a printed flyer DL size ( 210mmx99mm) for our Autism Consultancy website www.kowharaikids.nz which provides therapy for autistic children.
I want the flyer to look consistent with the website’s design. Please feel free to use the colour scheme, fonts, icons or any images from www.kowharaikids.nz.It should be easy to see “Autism” or “Autistic” word from a distance.
Please use either an oversized logo or make “Do you have a verbal and able autistic child?” more prominent.
Please do not convert the text fields to outlines, i.e. I need to be able to edit any text after.The final design should be either in Adobe Illustrator or Adobe Photoshop format.
The Specs for the flyer are
Document Trim Size99 x 210 mm 1169 x 2480 pixels
Full Bleed Size102 x 213 mm 1205 x 2516 pixels
Our Logo https://1drv.ms/u/s!AoH0rRjDY2GYg6QtU-xjoVlmslKp6gPlease
use this photo for the front side https://filevault.example/u/p8Jd2XcQw5Nv6LtK0rBg3aMf
another one for reverse
https://filevault.example/u/h4Ys7EnRb1Zo9GuP2wCk5jTl
Please use the following content:
Do you have a verbal and able autistic child?
We use child-centred, modern and innovative approaches
Teaching autistic children to bond, laugh and play.
We work with schools
We help autistic children to develop social minds
We offer:
• Specialist assessments
• Consultations for parents & schools
• Social learning programmes
• Social-cognitive therapy
We can create an individual learning path, best suited for your child.
Our programmes and interventions include:
• Bright Lanterns
• Kite Makers
• Pebble Circle
• Harbour Steps
• Puffin Pages
• Wexmoor Speech Ladder
• Tolvar Method
• PLOVIR Method
• Mirrorwood Echo Routine
contact details on both sides:
www.kowharaikids.nz
info@kowharaikids.nz
(09) 57-318-63

```html
<!DOCTYPE html>
<html lang="en">
<head>
<meta charset="utf-8">
<title>Kowharai Kids Consultancy – DL Flyer</title>
<link rel="stylesheet" href="https://fonts.googleapis.com/css2?family=Bubblegum+Sans&family=Source+Sans+3:wght@400;600&display=swap">
<style>
  :root{
    --teal:#52c4c4;
    --teal-deep:#3eaaad;
    --teal-light:#8fdcd8;
    --navy:#1f2d55;
    --yellow:#f8cf2b;
    --grey:#a3a3a3;
    --white:#ffffff;
    --stage:#ecebea;
    --display:'Bubblegum Sans', cursive;
    --body:'Source Sans 3', sans-serif;
  }
  *{box-sizing:border-box;margin:0;padding:0}
  html,body{width:1200px;height:1136px;overflow:hidden;background:var(--stage)}
  .canvas{position:relative;width:1200px;height:1136px}
  .flyer{position:absolute;top:81px;width:439px;height:930px;background:var(--white);overflow:hidden;box-shadow:0 4px 14px rgba(0,0,0,.18)}
  .flyer--front{left:107px}
  .flyer--back{left:647px}
  .photo{position:absolute;left:0;width:100%}
  .photo--front{top:95px;height:370px;background:linear-gradient(120deg,#c9b7a4 0%,#f1efe9 45%,#e7c86a 70%,#d9d2c6 100%)}
  .photo--back{top:0;height:330px;background:linear-gradient(135deg,#d8b98f 0%,#efe2cf 40%,#e9a7a3 70%,#9fc9dc 100%)}
  .shapes{position:absolute;inset:0;width:439px;height:930px}
  .brand{position:absolute;top:16px;left:0;width:100%;display:flex;justify-content:center;align-items:center;gap:14px}
  .brand__mark{width:54px;height:54px;border-radius:50%;background:var(--yellow)}
  .brand__name{font-family:var(--display);color:var(--navy);font-size:28px;line-height:1.05}
  .headline{position:absolute;top:500px;left:20px;right:20px;text-align:center;font-family:var(--display);color:var(--navy);font-size:27px;line-height:34px;letter-spacing:.5px}
  .rule{position:absolute;height:3px;background:var(--yellow)}
  .intro{position:absolute;top:597px;left:10px;right:10px;text-align:center;font-family:var(--body);color:var(--white);font-size:15.5px;line-height:25.2px}
  .offers{position:absolute;top:735px;left:0;width:100%;height:90px}
  .offer{position:absolute;width:90px;margin-left:-45px;text-align:center}
  .icon{width:50px;height:50px;border-radius:50%;border:2.5px solid var(--white);background:var(--teal);margin:0 auto;display:flex;align-items:center;justify-content:center;box-shadow:0 2px 3px rgba(0,0,0,.15)}
  .icon svg{width:28px;height:28px}
  .offer__label{font-family:var(--body);font-size:10px;line-height:12px;color:var(--navy);margin-top:6px}
  .call{position:absolute;top:857px;left:79px;width:279px;height:32px;border-radius:16px;background:var(--yellow);display:flex;align-items:center;justify-content:center;gap:8px;font-family:var(--display);color:var(--navy);font-size:19px;letter-spacing:.6px}
  .call svg{width:20px;height:20px}
  .contact{position:absolute;top:896px;left:0;width:100%;text-align:center;font-family:var(--body);font-size:16px;color:var(--navy)}
  .tagline{position:absolute;top:382px;left:40px;right:20px;display:flex;align-items:center;gap:22px}
  .tagline__mark{flex:none;width:48px;height:48px;border-radius:50%;background:var(--yellow)}
  .tagline__text{font-family:var(--display);color:var(--navy);font-size:17px;line-height:23px;letter-spacing:.4px}
  .programmes-title{position:absolute;top:490px;left:0;width:100%;text-align:center;font-family:var(--body);color:var(--white);font-size:18px}
  .programme{position:absolute;display:flex;align-items:center;gap:10px}
  .programme .icon{margin:0}
  .programme__label{font-family:var(--body);color:var(--navy);font-size:12px;line-height:16px;text-transform:uppercase;width:150px}
</style>
</head>
<body>
<div class="canvas">

  <!-- Front side -->
  <section class="flyer flyer--front">
    <div class="photo photo--front" role="img" aria-label="Photo: a therapist and a smiling boy holding a teddy bear in a bright playroom"></div>
    <svg class="shapes" viewBox="0 0 439 930" aria-hidden="true">
      <defs>
        <linearGradient id="tealFront" x1="0" y1="0" x2="0" y2="1">
          <stop offset="0" stop-color="#56c8c6"/><stop offset="1" stop-color="#3ea9ab"/>
        </linearGradient>
      </defs>
      <path d="M0 0H439V112C300 100 150 135 0 112Z" fill="#fff"/>
      <path d="M0 118C150 141 300 106 439 118" stroke="#a3a3a3" stroke-width="4" fill="none"/>
      <path d="M0 113C150 136 300 101 439 113" stroke="#f8cf2b" stroke-width="5" fill="none"/>
      <path d="M0 440C70 425 140 455 220 440S360 425 439 438V470H0Z" fill="#fff" opacity=".75"/>
      <path d="M0 452C80 438 150 468 225 453S370 440 439 452V930H0Z" fill="url(#tealFront)"/>
      <path d="M0 468C80 458 160 478 240 466S380 458 439 468V478C360 470 300 480 220 476S70 470 0 478Z" fill="#8fdcd8" opacity=".5"/>
      <path d="M0 836C150 822 300 822 439 838" stroke="#f8cf2b" stroke-width="5" fill="none"/>
      <path d="M0 842C150 828 300 828 439 844" stroke="#a3a3a3" stroke-width="4" fill="none"/>
      <path d="M0 846C150 832 300 832 439 848V930H0Z" fill="#fff"/>
    </svg>

    <div class="brand">
      <span class="brand__mark"></span>
      <span class="brand__name">Kowharai Kids<br>Consultancy</span>
    </div>

    <h1 class="headline">Do you have a verbal and able autistic child?</h1>
    <div class="rule" style="top:582px;left:103px;width:233px"></div>
    <p class="intro">We use child-centred, modern and innovative approaches<br>Teaching autistic children to bond, laugh and play<br>We work with schools<br>We help autistic children to develop social minds<br>We offer:</p>

    <div class="offers">
      <div class="offer" style="left:71px">
        <div class="icon"><svg viewBox="0 0 28 28" fill="none" stroke="#f8cf2b" stroke-width="2.2" stroke-linecap="round"><path d="M7 10A8 8 0 0 1 20 6"/><path d="M21 18A8 8 0 0 1 8 22"/></svg></div>
        <p class="offer__label">Specialist assessments</p>
      </div>
      <div class="offer" style="left:164px">
        <div class="icon"><svg viewBox="0 0 28 28" fill="#f8cf2b"><ellipse cx="11" cy="11" rx="9" ry="6.5"/><ellipse cx="18" cy="17" rx="8" ry="6" fill="#f8cf2b" stroke="#52c4c4" stroke-width="1.5"/></svg></div>
        <p class="offer__label">Consultations for parents &amp; schools</p>
      </div>
      <div class="offer" style="left:257px">
        <div class="icon"><svg viewBox="0 0 28 28" fill="none" stroke="#f8cf2b" stroke-width="2.2"><circle cx="11" cy="15" r="5"/><circle cx="19" cy="8" r="3.5"/><path d="M11 7v3M11 20v3M3 15h3M16 15h3"/></svg></div>
        <p class="offer__label">Social learning programmes</p>
      </div>
      <div class="offer" style="left:350px">
        <div class="icon"><svg viewBox="0 0 28 28" fill="none" stroke="#f8cf2b" stroke-width="2.2" stroke-linecap="round"><circle cx="14" cy="6" r="2.5"/><path d="M13 8L6 24M15 8L22 24M8 17h12"/></svg></div>
        <p class="offer__label">Social-cognitive therapy</p>
      </div>
    </div>

    <div class="call">CALL US
      <svg viewBox="0 0 20 20"><circle cx="10" cy="10" r="9" fill="none" stroke="#1f2d55" stroke-width="1.8"/><path d="M7 5.5l1.6 2.4-1 1.1c.6 1.3 1.6 2.3 2.9 2.9l1.1-1 2.4 1.6-.8 1.6c-3.6-.3-7.1-3.8-7.4-7.4z" fill="#1f2d55"/></svg>
      (09) 57-318-63</div>
    <p class="contact">info@kowharaikids.nz &nbsp;|&nbsp; www.kowharaikids.nz</p>
  </section>

  <!-- Reverse side -->
  <section class="flyer flyer--back">
    <div class="photo photo--back" role="img" aria-label="Photo: a boy in a striped shirt playing with toy cars on a wooden floor"></div>
    <svg class="shapes" viewBox="0 0 439 930" aria-hidden="true">
      <defs>
        <linearGradient id="tealBack" x1="0" y1="0" x2="0" y2="1">
          <stop offset="0" stop-color="#56c8c6"/><stop offset="1" stop-color="#3ea9ab"/>
        </linearGradient>
      </defs>
      <path d="M0 304C70 290 140 318 220 304S360 290 439 302V340H0Z" fill="#fff" opacity=".75"/>
      <path d="M0 316C80 302 150 332 225 317S370 304 439 316V930H0Z" fill="url(#tealBack)"/>
      <path d="M0 332C80 322 160 342 240 330S380 322 439 332V342C360 334 300 344 220 340S70 334 0 342Z" fill="#8fdcd8" opacity=".5"/>
      <path d="M0 836C150 822 300 822 439 838" stroke="#f8cf2b" stroke-width="5" fill="none"/>
      <path d="M0 842C150 828 300 828 439 844" stroke="#a3a3a3" stroke-width="4" fill="none"/>
      <path d="M0 846C150 832 300 832 439 848V930H0Z" fill="#fff"/>
    </svg>

    <div class="tagline">
      <span class="tagline__mark"></span>
      <p class="tagline__text">We can create an individual learning path, best suited for your child.</p>
    </div>
    <div class="rule" style="top:473px;left:47px;width:344px"></div>
    <p class="programmes-title">Our programmes and interventions include:</p>

    <div class="programme" style="left:21px;top:541px">
      <div class="icon"><svg viewBox="0 0 28 28" fill="none" stroke="#f8cf2b" stroke-width="2"><circle cx="14" cy="12" r="5"/><path d="M12 19h4M12 22h4M14 3v2M5 12h2M21 12h2"/></svg></div>
      <span class="programme__label">Bright Lanterns /<br>Kite Makers</span>
    </div>
    <div class="programme" style="left:21px;top:608px">
      <div class="icon"><svg viewBox="0 0 28 28" fill="none" stroke="#f8cf2b" stroke-width="2"><circle cx="14" cy="8" r="4.5"/><circle cx="8" cy="19" r="4.5"/><circle cx="20" cy="19" r="4.5"/></svg></div>
      <span class="programme__label">Pebble<br>Circle</span>
    </div>
    <div class="programme" style="left:21px;top:673px">
      <div class="icon"><svg viewBox="0 0 28 28"><ellipse cx="14" cy="13" rx="11" ry="8.5" fill="none" stroke="#f8cf2b" stroke-width="2"/><path d="M14 17l-4-4a2.2 2.2 0 0 1 4-2.2A2.2 2.2 0 0 1 18 13z" fill="#f8cf2b"/></svg></div>
      <span class="programme__label">Harbour<br>Steps</span>
    </div>
    <div class="programme" style="left:21px;top:740px">
      <div class="icon"><svg viewBox="0 0 28 28" fill="none" stroke="#f8cf2b" stroke-width="2"><path d="M3 7h9a2 2 0 0 1 2 2v13a2 2 0 0 0-2-2H3zM25 7h-9a2 2 0 0 0-2 2v13a2 2 0 0 1 2-2h9z"/></svg></div>
      <span class="programme__label">Puffin<br>Pages</span>
    </div>

    <div class="programme" style="left:236px;top:541px">
      <div class="icon"><svg viewBox="0 0 28 28" fill="#f8cf2b"><ellipse cx="13" cy="14" rx="10" ry="7"/></svg></div>
      <span class="programme__label">Wexmoor<br>Speech Ladder</span>
    </div>
    <div class="programme" style="left:236px;top:608px">
      <div class="icon"><svg viewBox="0 0 28 28" fill="none" stroke="#f8cf2b" stroke-width="3" stroke-linecap="round"><path d="M8 6l12 16M20 6L8 22"/></svg></div>
      <span class="programme__label">Tolvar<br>Method</span>
    </div>
    <div class="programme" style="left:236px;top:673px">
      <div class="icon"><svg viewBox="0 0 28 28" fill="#f8cf2b"><path d="M6 22C6 12 12 5 22 5C22 15 16 22 6 22Z"/></svg></div>
      <span class="programme__label">PLOVIR<br>Method</span>
    </div>
    <div class="programme" style="left:236px;top:740px">
      <div class="icon"><svg viewBox="0 0 28 28" fill="none" stroke="#f8cf2b" stroke-width="2.4" stroke-linecap="round"><path d="M14 4v14M7 11h14M9 18a5 5 0 0 0 10 0"/></svg></div>
      <span class="programme__label">Mirrorwood<br>Echo Routine</span>
    </div>

    <div class="call">CALL US
      <svg viewBox="0 0 20 20"><circle cx="10" cy="10" r="9" fill="none" stroke="#1f2d55" stroke-width="1.8"/><path d="M7 5.5l1.6 2.4-1 1.1c.6 1.3 1.6 2.3 2.9 2.9l1.1-1 2.4 1.6-.8 1.6c-3.6-.3-7.1-3.8-7.4-7.4z" fill="#1f2d55"/></svg>
      (09) 57-318-63</div>
    <p class="contact">info@kowharaikids.nz &nbsp;|&nbsp; www.kowharaikids.nz</p>
  </section>

</div>
</body>
</html>
```